Halvorsen Basin Holdings, LP Letter Head

We need an official company letter head design that is clean and mimics our company logo style. It will include our logo, address, phone, and website. We are an OIl and Gas mineral purchasing company, so hints of oil rigs or related design would be desirable.

Industry/Entity Type

Oil And Gas

Colors
ec1f27
f04a50
f59195
fbd4d5

Requirements
Must have
• Logo
• 7316 Marwick T. Ellsbury Parkway, Suite 418
• Dallas TX, 75391
• 214-763-1957
• www.halvorsenbasin.com
Nice to have
• Oil Rigs or OIl and gas related design

```html
<!DOCTYPE html>
<html lang="en">
<head>
<meta charset="utf-8">
<title>Halvorsen Basin Holdings – Letterhead and Folder</title>
<link href="https://fonts.googleapis.com/css2?family=Cinzel:wght@500&family=Didact+Gothic&family=EB+Garamond:wght@400;600&display=swap" rel="stylesheet">
<style>
  :root {
    --brand-red: #d71d24;
    --brand-red-bright: #ec1f27;
    --brand-red-soft: #f59195;
    --brand-red-pale: #fbd4d5;
    --ink: #3a3a3a;
    --ink-dark: #222;
    --rule: #333;
    --paper: #ffffff;
    --folder: #f1f1f1;
    --backdrop: #e9e9e9;
    --rig-grey: #c9c9c9;
  }
  * { box-sizing: border-box; margin: 0; padding: 0; }
  html, body { width: 1200px; height: 894px; overflow: hidden; }
  body { background: var(--backdrop); position: relative; font-family: "Didact Gothic", sans-serif; }

  .letterhead {
    position: absolute; left: 74px; top: 73px; width: 522px; height: 675px;
    background: var(--paper); overflow: hidden;
  }
  .brand { position: absolute; left: 0; right: 0; top: 27px; text-align: center; }
  .brand-square {
    display: block; margin: 0 auto 10px; width: 34px; height: 34px;
    background: var(--brand-red);
  }
  .brand-name {
    font-family: "Cinzel", serif; font-weight: 500; color: var(--brand-red);
    line-height: 1.05;
  }
  .brand-name .line-1 { display: block; font-size: 26px; letter-spacing: 1px; }
  .brand-name .line-2 { display: block; font-size: 11.5px; letter-spacing: 4.5px; margin-top: 2px; }
  .header-rule {
    position: absolute; top: 125px; height: 1px; background: var(--rule);
  }
  .header-rule.left { left: 45px; width: 124px; }
  .header-rule.right { right: 45px; width: 124px; }

  .watermark-square {
    position: absolute; left: 157px; top: 212px; width: 240px; height: 240px;
    border: 5px solid var(--brand-red-pale); opacity: .6;
  }

  .letter-body {
    position: absolute; left: 55px; top: 159px; width: 411px;
    font-size: 10.8px; line-height: 17.1px; color: var(--ink); text-align: justify;
  }
  .letter-body p + p { margin-top: 17px; }

  .rig-scene {
    position: absolute; left: 170px; top: 470px; width: 352px; height: 178px;
    background: linear-gradient(180deg, rgba(201,201,201,0) 0%, rgba(201,201,201,.55) 45%, rgba(201,201,201,.85) 100%);
  }

  .signature { position: absolute; left: 380px; top: 584px; color: var(--ink-dark); }
  .signature .name { font-size: 13px; }
  .signature .title { font-size: 9px; margin-top: 6px; }

  .contact-line {
    position: absolute; left: 0; right: 0; top: 635px; text-align: center;
    font-family: "EB Garamond", serif; font-size: 6.6px; color: var(--ink-dark);
  }
  .contact-line .dot {
    display: inline-block; width: 3px; height: 3px; border-radius: 50%;
    background: var(--brand-red-bright); margin: 0 4px; vertical-align: middle;
  }
  .footer-band {
    position: absolute; left: 0; right: 0; bottom: 0; height: 27px;
    background: var(--brand-red); color: #fff; text-align: center;
    font-family: "EB Garamond", serif; font-weight: 600; font-size: 9px;
    letter-spacing: 2.2px; line-height: 27px;
  }

  .folder {
    position: absolute; left: 639px; top: 71px; width: 498px; height: 678px;
    background: linear-gradient(180deg, #f4f4f4, var(--folder));
    border-radius: 14px;
  }
  .folder-brand { position: absolute; left: 0; right: 0; top: 455px; text-align: center; }
  .folder-brand .brand-square { width: 60px; height: 60px; margin-bottom: 16px; }
  .folder-brand .line-1 { font-size: 40px; letter-spacing: 1.5px; }
  .folder-brand .line-2 { font-size: 17px; letter-spacing: 7px; margin-top: 4px; }
</style>
</head>
<body>

<section class="letterhead" aria-label="Letterhead">
  <div class="watermark-square" aria-hidden="true"></div>

  <header class="brand">
    <span class="brand-square" aria-hidden="true"></span>
    <div class="brand-name">
      <span class="line-1">HALVORSEN</span>
      <span class="line-2">BASIN HOLDINGS</span>
    </div>
  </header>
  <span class="header-rule left"></span>
  <span class="header-rule right"></span>

  <div class="rig-scene" role="img" aria-label="Faded grey silhouette of an offshore oil rig and derrick"></div>

  <div class="letter-body">
    <p>Lorem ipsum dolor sit amet, consectetur adipiscing elit. Donec orci purus, luctus vitae dignissim eu, iaculis sed purus. Vivamus faucibus, ipsum nec aliquet viverra, leo mauris condimentum ligula, sit amet sagittis enim ligula quis arcu. Nam egestas tortor id nisi porttitor mattis. In tortor ante, ultricies in suscipit a, tempus non massa. Vivamus et auctor mi. Fusce vel massa nulla. Phasellus nec eros mauris, et scelerisque orci. Donec malesuada orci vitae nulla accumsan porta a id massa.</p>
    <p>Quisque accumsan iaculis magna sit amet fringilla. Maecenas consequat, magna eget tincidunt semper, odio nibh rutrum mi, id feugiat ante nisi eu risus. Vestibulum nunc orci, rhoncus a placerat in, ultricies in mi. Cras mattis varius eros, vel fringilla nisi suscipit eget. Quisque scelerisque sagittis nulla at porttitor. Mauris a justo et tellus interdum tristique. Sed id augue vitae urna euismod commodo aliquet a quam. Pellentesque arcu velit, cursus et malesuada ut, consequat et diam. Nullam erat sem, rhoncus id ullamcorper vitae, rhoncus et arcu. In ultricies ultricies nulla,</p>
    <p>Kut rutrum nisi iaculis at. Donec eu magna a metus ornare faucibus. Fusce aliquet faucibus ultricies. Morbi semper, est id tincidunt gravida, sem arcu adipiscing lacus, ac bibendum nulla leo eu purus. Quisque nec diam sed risus consectetur a ccumsan quis quis nibh. Vestibulum id purus lorem. Donec eu magna a metus ornare faucibus. Fusce aliquet faucibus ultricies. Morbi semper, est id tincidunt gravida, sem arcu adipiscing lacus, ac bibendum nulla leo eu purus. Quisque nec diam sed risus consectetur a ccumsan quis quis nibh. Vestibulum id purus lorem.</p>
  </div>

  <div class="signature">
    <div class="name">Dana Whitfield</div>
    <div class="title">Co-Founder &amp; CEO</div>
  </div>

  <div class="contact-line">
    Phone: 214-763-1957<span class="dot"></span>7316 Marwick T. Ellsbury Parkway, Suite 418, Dallas TX, 75391
  </div>
  <footer class="footer-band">www.halvorsenbasin.com</footer>
</section>

<section class="folder" aria-label="Presentation folder cover">
  <div class="brand folder-brand">
    <span class="brand-square" aria-hidden="true"></span>
    <div class="brand-name">
      <span class="line-1">HALVORSEN</span>
      <span class="line-2">BASIN HOLDINGS</span>
    </div>
  </div>
</section>

</body>
</html>
```